Corporate Branding - Web and Print

A UK based company will like to use an existing logo to create branding materials for all marketing related documents, including business card, prints, letterhead, Website, Twitter, Facebook, Instagram logo etc. This company serves high-end clientele in the fashion, health and wellness and as such high quality and class is of utmost importance.
Where the logo can be modernised without losing its character then experiment. The main thing is to have a corporate branding which can be used later for brochures, Business Plan infographics.
The prominent colour within the organisation is burnt orange with no secondary colour. However if you believe a secondary colour is needed then use it, otherwise keep it simple and classy. Any chosen colours have to match perfectly.
Target Market(s)
High net worth individuals
Industry/Entity Type
Health And Wellness
Contact Information for Business Card
classy

```html
<!DOCTYPE html>
<html lang="en">
<head>
<meta charset="utf-8">
<title>Varelle — Business Card</title>
<link href="https://fonts.googleapis.com/css2?family=Source+Sans+3:wght@400;600;700&display=swap" rel="stylesheet">
<style>
  :root {
    --burnt-orange: #f7941e;
    --card-white: #ffffff;
    --text-grey: #6d6e71;
    --backdrop: #3b3b3b;
  }
  * { margin: 0; padding: 0; box-sizing: border-box; }
  html, body {
    width: 1200px; height: 864px; overflow: hidden;
    background: var(--backdrop);
    font-family: "Source Sans 3", sans-serif;
  }
  .stage { position: relative; width: 1200px; height: 864px; }
  .card {
    position: absolute; top: 313px;
    width: 420px; height: 240px;
    border-radius: 13px;
    box-shadow: 0 6px 14px rgba(0,0,0,0.45);
  }
  .card-front { left: 174px; background: var(--card-white); }
  .card-back { left: 606px; background: var(--burnt-orange); }

  .brand {
    position: absolute; left: 46px; top: 104px;
    width: 150px; display: flex; align-items: center; justify-content: center; gap: 8px;
    color: var(--burnt-orange);
    font-weight: 700; font-size: 27px; letter-spacing: 1px; line-height: 1;
  }
  .brand-dot { width: 14px; height: 14px; border-radius: 50%; background: var(--burnt-orange); flex: none; }

  .divider {
    position: absolute; left: 211px; top: 69px;
    width: 2px; height: 101px; background: var(--burnt-orange);
  }
  .contact { position: absolute; left: 228px; top: 66px; }
  .contact-name { color: var(--burnt-orange); font-weight: 600; font-size: 17px; line-height: 1.1; }
  .contact-role { color: var(--text-grey); font-size: 12px; line-height: 1.3; margin-bottom: 13px; }
  .contact-list { list-style: none; }
  .contact-list li {
    display: flex; align-items: center; gap: 4px;
    color: var(--text-grey); font-size: 11.5px; line-height: 14.4px;
  }
  .contact-list svg { width: 9px; height: 9px; flex: none; }

  .back-brand {
    position: absolute; left: 0; right: 0; top: 100px;
    display: flex; align-items: center; justify-content: center; gap: 10px;
    color: var(--card-white); font-weight: 700; font-size: 32px; letter-spacing: 1.5px; line-height: 1;
  }
  .back-brand .brand-dot { width: 16px; height: 16px; background: var(--card-white); }
  .back-web {
    position: absolute; left: 0; right: 0; top: 206px; text-align: center;
    color: var(--card-white); font-size: 11.5px; font-weight: 600;
  }
</style>
</head>
<body>
<div class="stage">
  <section class="card card-front">
    <div class="brand"><span class="brand-dot"></span>VARELLE</div>
    <div class="divider"></div>
    <div class="contact">
      <p class="contact-name">Daniel Hart</p>
      <p class="contact-role">President</p>
      <ul class="contact-list">
        <li><svg viewBox="0 0 10 10"><path d="M2 0.5 L3.6 2.6 L2.7 3.6 Q3.8 5.9 6.3 7.2 L7.3 6.3 L9.5 7.9 L8.4 9.5 Q2.5 8.6 0.5 1.6 Z" fill="var(--burnt-orange)"/></svg>020 7946 0321</li>
        <li><svg viewBox="0 0 10 10"><rect x="2.5" y="0.5" width="5" height="9" rx="1" fill="none" stroke="var(--burnt-orange)" stroke-width="1.2"/></svg>07700 900 482</li>
        <li><svg viewBox="0 0 10 10"><rect x="0.5" y="2" width="9" height="6" fill="var(--burnt-orange)"/><path d="M0.5 2 L5 5.5 L9.5 2" fill="none" stroke="#fff" stroke-width="0.8"/></svg>hello@varelle-studio.co.uk</li>
        <li><svg viewBox="0 0 10 10"><g fill="none" stroke="var(--burnt-orange)" stroke-width="0.9"><circle cx="5" cy="5" r="4.3"/><ellipse cx="5" cy="5" rx="1.9" ry="4.3"/><path d="M0.7 5 H9.3"/></g></svg>varelle-studio.co.uk</li>
      </ul>
    </div>
  </section>

  <section class="card card-back">
    <div class="back-brand"><span class="brand-dot"></span>VARELLE</div>
    <p class="back-web">www.varelle-studio.co.uk</p>
  </section>
</div>
</body>
</html>
```